Wellspring Renewal Collective Botswana Africa Flyer

Create an A5 double sided flyer to advertise a campus lifestyle wellness training at the university of Tselakgang. This flyer invite all interested to freely attend naturopathic treatment training, stop addiction training, music therapy training lessons. Conducted by Wellspring Renewal Collective. The lead facilitator is Marisol-Ann Okoye.
Flyer text available at 'must haves'

Target Market(s)

University students

Industry/Entity Type

Training

Requirements
Must have
• Logo (supplied)
• Picture of Marisol-Ann Okoye, our Lead Facilitator (supplied)
• Music pic. Classical hym choir or preferably orchestra of predominantly black youth
• And the text must be as follows:
• WELLSPRING RENEWAL COLLECTIVE (WRC) is a non profit organization that conducts wholistic health programs in Universities aimed at reversing Lifestyle Diseases and breaking down the chains of Drug Addiction and Satanism among the youth. We conduct a 3 hour practical training every week on disease treatment protocols, stop addiction and music therapy.
• 1. Disease Treatment Programs: We thoroughly train you to use food, herbs, natural remedies and scientifically proven lifestyle changes to reverse lifestyle diseases such as diabetes, arthritis, cancer and hypertension.
• 2. Stop Addiction Programs: We also teach you how to administer a 10 day treatment protocol to wipe out the craving for drugs such cocaine, marijuana and tobacco, and to also rehabilitate those freed from these addictions.
• 3. Music Therapy: Top notch musical training will equip you to efficiently administer music therapy to heal the soul and relief tensions in any community using voice and musical instruments. Music, when properly done, heals both the singer and the one to whom it is sung!
• These training protocols will not only help you but most importantly will equip you to effectively help others!
• THE MUSIC CONNECTION
• Music is part of our being. There is a kind of music that goes to the waist igniting in us the desire for illicit sex, drugs and all recklessness. And there is a type of music that touches the heart and bring us closer to our Maker, igniting feelings of sympathy, kindness and generosity to our fellow man.
• When we are happy, a song always says it best. When we are sad, music has a way of saying it in ways that words would never reach. And when there is a call to action, a cause to which the sleeping needs to be awakened, music makes a perfect wake up call!
• The cause of WRC is a liberation struggle that cannot do without music. For when the chains of addiction are broken down, the joy that comes cannot be expressed in talking tones. And since it was through music that our captivity was perpetuated, it's only befitting that our liberation must be sustained through song. It is a new song though, which we shall first learn to sing in voice, and then through musical instruments of harps, violins and keyboards. A Quadrangle Ensemble of Daybreak, singing Meadowlight Hymns! You ought to be a part of it!
• THIS VALUABLE TRAINING THAT IS WORTH LOTS OF MONEY ELSEWHERE IS NOW BROUGHT TO YOU FREE OF CHARGE. TO ENROLL IMMEDIATELY CALL 71450362 or EMAIL: WRC2016@kelvora.com

```html
<!DOCTYPE html>
<html lang="en">
<head>
<meta charset="utf-8">
<title>Wellspring Renewal Collective – Campus Wellness Flyer</title>
<link href="https://fonts.googleapis.com/css2?family=Questrial&family=Montserrat:wght@600;700&display=swap" rel="stylesheet">
<style>
  :root{
    --bg:#ecebe8;
    --paper:#ffffff;
    --red:#e31e24;
    --green:#12924a;
    --ink:#1d1d1b;
    --stage-dark:#241a2e;
    --stage-mid:#3d5a3a;
    --stage-warm:#7a4a2e;
  }
  *{margin:0;padding:0;box-sizing:border-box;}
  html,body{width:1200px;height:1200px;overflow:hidden;background:var(--bg);}
  body{position:relative;font-family:"Questrial",sans-serif;color:var(--ink);}

  .flyer{position:absolute;top:212px;width:544px;height:775px;background:var(--paper);overflow:hidden;box-shadow:0 2px 10px rgba(0,0,0,.18);}
  .flyer--front{left:37px;}
  .flyer--back{left:619px;}

  .flyer__header{position:absolute;left:0;top:0;width:544px;height:280px;}

  .brand{position:absolute;display:flex;align-items:center;gap:8px;}
  .brand__dot{width:26px;height:26px;border-radius:50%;background:var(--red);flex:none;}
  .brand__name{font-family:"Montserrat",sans-serif;font-weight:700;font-size:13px;line-height:1.2;color:var(--green);letter-spacing:.3px;}
  .flyer--front .brand{left:372px;top:34px;width:160px;}
  .flyer--back .brand{left:350px;top:54px;width:180px;}

  .portrait{position:absolute;left:405px;top:127px;width:96px;height:114px;border:3px solid var(--red);border-radius:8px;background:linear-gradient(160deg,#f4e6da,#c79c82 60%,#7b5441);}

  .copy{position:absolute;font-size:14.2px;line-height:19.4px;text-align:justify;}
  .copy p{margin-bottom:19px;}
  .flyer--front .copy{left:46px;top:266px;width:446px;}
  .flyer--back .copy{left:52px;top:274px;width:444px;}
  .accent{color:var(--red);}

  .section-title{position:absolute;left:128px;top:220px;width:288px;height:36px;background:var(--green);border:3px solid var(--red);border-radius:6px;color:#fff;font-family:"Montserrat",sans-serif;font-weight:600;font-size:19px;line-height:30px;text-align:center;letter-spacing:.3px;}

  .footer-wave{position:absolute;left:0;bottom:0;width:544px;height:50px;}

  .cta{position:absolute;left:0;bottom:0;width:544px;height:78px;background:var(--red);color:#fff;text-align:center;font-size:14.4px;line-height:19px;padding-top:13px;letter-spacing:.2px;}
  .cta__rule{position:absolute;left:0;bottom:78px;width:544px;height:7px;background:var(--green);}
</style>
</head>
<body>

<section class="flyer flyer--front">
  <svg class="flyer__header" viewBox="0 0 544 280" width="544" height="280">
    <defs>
      <linearGradient id="stageFront" x1="0" y1="0" x2="1" y2="1">
        <stop offset="0" stop-color="var(--stage-mid)"/>
        <stop offset=".55" stop-color="var(--stage-dark)"/>
        <stop offset="1" stop-color="var(--stage-warm)"/>
      </linearGradient>
    </defs>
    <rect role="img" aria-label="Photo of musicians performing on stage with guitar and microphone" x="0" y="0" width="544" height="240" fill="url(#stageFront)"/>
    <path d="M330 0 H544 V262 C470 250 400 222 372 165 C348 115 332 55 330 0 Z" fill="var(--paper)"/>
    <path d="M0 203 C160 192 320 212 544 248 V262 C350 240 150 226 0 232 Z" fill="var(--red)"/>
    <path d="M0 232 C150 226 350 240 544 262 V280 H0 Z" fill="var(--paper)"/>
  </svg>

  <div class="brand">
    <span class="brand__dot"></span>
    <span class="brand__name">WELLSPRING RENEWAL COLLECTIVE</span>
  </div>
  <div class="portrait" role="img" aria-label="Portrait of lead facilitator Marisol-Ann Okoye"></div>

  <div class="copy">
    <p><span class="accent">WELLSPRING RENEWAL COLLECTIVE (WRC)</span> is a non profit organization that conducts wholistic health programs in Universities aimed at reversing Lifestyle Diseases and breaking down the chains of Drug Addiction and Satanism among the youth. We conduct a 3 hour practical training every week on disease treatment protocols, stop addiction and music therapy.</p>
    <p><span class="accent">1.</span> Disease Treatment Programs: We thoroughly train you to use food, herbs, natural remedies and scientifically proven lifestyle changes to reverse lifestyle diseases such as diabetes, arthritis, cancer and hypertension.</p>
    <p><span class="accent">2.</span> Stop Addiction Programs: We also teach you how to administer a 10 day treatment protocol to wipe out the craving for drugs such cocaine, marijuana and tobacco, and to also rehabilitate those freed from these addictions.</p>
    <p><span class="accent">3.</span> Music Therapy: Top notch musical training will equip you to efficiently administer music therapy to heal the soul and relief tensions in any community using voice and musical instruments. Music, when properly done, heals both the singer and the one to whom it is sung!</p>
    <p>These training protocols will not only help you but most importantly will equip you to effectively help others!</p>
  </div>

  <svg class="footer-wave" viewBox="0 0 544 50" width="544" height="50">
    <path d="M0 18 C180 4 360 4 544 20 V24 C360 9 180 9 0 23 Z" fill="var(--red)"/>
    <path d="M0 23 C180 9 360 9 544 24 V50 H0 Z" fill="var(--green)"/>
  </svg>
</section>

<section class="flyer flyer--back">
  <svg class="flyer__header" viewBox="0 0 544 280" width="544" height="280">
    <defs>
      <linearGradient id="stageBack" x1="0" y1="0" x2="1" y2="1">
        <stop offset="0" stop-color="#3a2622"/>
        <stop offset=".6" stop-color="#5c3a30"/>
        <stop offset="1" stop-color="#9a8a80"/>
      </linearGradient>
    </defs>
    <rect role="img" aria-label="Photo of a musician playing a stringed instrument on a lit stage" x="0" y="0" width="544" height="200" fill="url(#stageBack)"/>
    <path d="M290 0 H544 V190 C470 186 400 175 355 140 C318 110 296 60 290 0 Z" fill="var(--paper)"/>
    <path d="M0 178 C140 186 300 190 430 196 C340 196 160 194 0 198 Z" fill="var(--red)"/>
    <path d="M0 198 C160 194 340 196 544 196 V280 H0 Z" fill="var(--paper)"/>
  </svg>

  <div class="brand">
    <span class="brand__dot"></span>
    <span class="brand__name">WELLSPRING RENEWAL COLLECTIVE</span>
  </div>

  <h2 class="section-title">THE MUSIC CONNECTION</h2>

  <div class="copy">
    <p>Music is part of our being. There is a kind of music that goes to the waist igniting in us the desire for illicit sex, drugs and all recklessness. And there is a type of music that touches the heart and bring us closer to our Maker, igniting feelings of sympathy, kindness and generosity to our fellow man.</p>
    <p>When we are happy, a song always says it best. When we are sad, music has a way of saying it in ways that words would never reach. And when there is a call to action, a cause to which the sleeping needs to be awakened, music makes a perfect wake up call!</p>
    <p>The cause of WRC is a liberation struggle that cannot do without music. For when the chains of addiction are broken down, the joy that comes cannot be expressed in talking tones. And since it was through music that our captivity was perpetuated, it's only befitting that our liberation must be sustained through song. It is a new song though, which we shall first learn to sing in voice, and then through musical instruments of harps, violins and keyboards. A Quadrangle Ensemble of Daybreak, singing Meadowlight Hymns! You ought to be a part of it!</p>
  </div>

  <div class="cta__rule"></div>
  <div class="cta">THIS VALUABLE TRAINING THAT IS WORTH LOTS OF MONEY ELSEWHERE IS NOW BROUGHT TO YOU FREE OF CHARGE. TO ENROLL IMMEDIATELY CALL 71450362 or EMAIL:</div>
</section>

</body>
</html>
```